Simple Business Cards for Self-employed Coach

Simple business card with a design that includes the QLT logo.
Using either only the logo color or additional colors that match the logo.

Meridian Guides reach deeply into the past, gathering wisdom from East and West, while still staying current with the frontiers of new discovery in cognitive science, genetics, and other disciplines. see https://www.brightharborpath.example/what-is-integral-coaching/

Target Market(s)

Coaching Clients in Tokyo /Asia; in business organizations, but also outside

Industry/Entity Type

Life Coaching

Contact Information for Business Card

Lukas Brenning
Certified Meridian Guide

3-2-48 Kamiyoshi
Nakarino 164-0392
Tokyo, Japan

Phone: +81 70 4817 5062
E-Mail: lukas.brenning@mailora.example

Font styles to use
Sans Serif

Colors
00a990

Requirements
Must have
• include uploaded logo
• color fitting with QLT logo color
Nice to have
• simple, elegant design
Should not have
• clutter

```html
<!DOCTYPE html>
<html lang="en">
<head>
<meta charset="utf-8">
<title>QLT Business Card</title>
<link rel="stylesheet" href="https://fonts.googleapis.com/css2?family=Open+Sans:wght@400;600&display=swap">
<style>
  :root {
    --teal: #00a990;
    --teal-deep: #005a4c;
    --panel-dark: #01332c;
    --paper: #f6f9f9;
    --stage: #e4e4e4;
    --white: #ffffff;
  }
  * { box-sizing: border-box; margin: 0; padding: 0; }
  html, body { width: 1200px; height: 1200px; overflow: hidden; }
  body {
    background: var(--stage);
    font-family: "Open Sans", sans-serif;
    position: relative;
  }
  .card {
    position: absolute;
    left: 100px; top: 312px;
    width: 1000px; height: 575px;
    background: var(--paper);
    border: 3px solid #c9cbcb;
    overflow: hidden;
  }
  .card__panel { position: absolute; inset: 0; width: 100%; height: 100%; }
  .brand {
    position: absolute; left: 63px; top: 115px;
    display: flex; align-items: center; gap: 16px;
  }
  .brand__mark { width: 44px; height: 44px; background: var(--teal); }
  .brand__name {
    font-size: 60px; font-weight: 600; color: var(--teal);
    letter-spacing: 10px; line-height: 1;
  }
  .identity {
    position: absolute; left: 0; width: 425px; top: 307px;
    text-align: center;
  }
  .identity__name { font-size: 39px; font-weight: 600; color: var(--teal); line-height: 1.3; }
  .identity__title { font-size: 31px; font-weight: 600; color: var(--teal-deep); line-height: 1.4; }
  .contact { position: absolute; left: 510px; top: 148px; list-style: none; }
  .contact__item {
    display: flex; align-items: flex-start; gap: 12px;
    color: var(--white); font-size: 30px; line-height: 1.33;
    position: absolute; left: 0; white-space: nowrap;
  }
  .contact__item--email { top: 0; font-size: 23px; }
  .contact__item--email .contact__text { padding-top: 13px; }
  .contact__item--phone { top: 100px; }
  .contact__item--address { top: 193px; }
  .contact__icon { width: 60px; height: 60px; flex: none; }
  .contact__text { padding-top: 8px; }
  .contact__item--address .contact__text { padding-top: 4px; padding-left: 10px; }
</style>
</head>
<body>
  <section class="card" aria-label="QLT business card">
    <svg class="card__panel" viewBox="0 0 600 345" preserveAspectRatio="none" role="img" aria-label="Curved teal side panel">
      <defs>
        <linearGradient id="panelShade" x1="0" y1="0" x2="1" y2="0">
          <stop offset="0" stop-color="var(--panel-dark)"/>
          <stop offset="0.45" stop-color="var(--teal)"/>
          <stop offset="1" stop-color="var(--teal)"/>
        </linearGradient>
      </defs>
      <path d="M275,0 C235,60 222,200 312,345 L600,345 L600,0Z" fill="url(#panelShade)"/>
    </svg>

    <div class="brand">
      <span class="brand__mark"></span>
      <span class="brand__name">QLT</span>
    </div>

    <div class="identity">
      <p class="identity__name">Lukas Brenning</p>
      <p class="identity__title">Certified Meridian Guide</p>
    </div>

    <ul class="contact">
      <li class="contact__item contact__item--email">
        <svg class="contact__icon" viewBox="0 0 60 60" aria-hidden="true">
          <circle cx="30" cy="30" r="27" fill="none" stroke="#fff" stroke-width="3"/>
          <rect x="17" y="21" width="26" height="18" fill="#fff"/>
          <path d="M17,21 L30,32 L43,21 M17,39 L26,29 M43,39 L34,29" fill="none" stroke="var(--teal)" stroke-width="2"/>
        </svg>
        <span class="contact__text">lukas.brenning@mailora.example</span>
      </li>
      <li class="contact__item contact__item--phone">
        <svg class="contact__icon" viewBox="0 0 60 60" aria-hidden="true">
          <circle cx="30" cy="30" r="27" fill="none" stroke="#fff" stroke-width="3"/>
          <path d="M22,17 L27,17 L29,24 L25.5,27 C27.5,31 29.5,33 33,35 L36,31.5 L43,33.5 L43,38.5 C43,41 41,42 38,42 C28,41 19,32 18,22 C18,19 19,17 22,17Z" fill="#fff"/>
        </svg>
        <span class="contact__text">+81 70 4817 5062</span>
      </li>
      <li class="contact__item contact__item--address">
        <svg class="contact__icon" viewBox="0 0 60 60" aria-hidden="true">
          <circle cx="30" cy="30" r="27" fill="none" stroke="#fff" stroke-width="3"/>
          <path d="M15,30 L30,17 L45,30 L41,30 L41,42 L34,42 L34,34 L26,34 L26,42 L19,42 L19,30Z" fill="#fff"/>
        </svg>
        <span class="contact__text">3-2-48 Kamiyoshi<br>Nakarino 164-0392<br>Tokyo, Japan</span>
      </li>
    </ul>
  </section>
</body>
</html>
```